Business card design needed

Looking for an innovative design that portrays a professional image for our company. We are a structural steel erection, EWP and crane hire company. We are looking at having business and contact details on front of card and perhaps a list of what we hire on the back of the card. Our company machine colours are royal blue and silver at present but would be open to change with our cards...
Updates
We are looking for double sided designs due to the amount of information required on the card
The Logo uploaded if the logo we have been using, however our company name has changed to just "Stoneridge Lifting Works". I have uploaded the image just for ideas...
Reason: Allowing more time for more design submissions
Reason: Want more dedigns
Target Market(s)
Construction/Industrial
Industry/Entity Type
Structural Steel
Contact Information for Business Card
Business Name: Stoneridge Lifting Works
Specialising in Structural Steel Erection, Equipment & Crane Hire
Address: 27 Carvell Street, Mondarra Q 4612
Site Contact: Danny Pruett - 0491 637 205 - dan@slwlifting.com
Office Contact: Leoni Marsh - 0437 918 542 - leoni@slwlifting.com
We hire Forklifts, Telehandlers, Scissor-lifts, Boom-lifts, 3T Mini Cranes, 16T/20T Kelvo, Prime mover with extendable trailer (13.5-22m), Qualified Boilermakers,Riggers and Dogman.
Logo Text
Stoneridge Lifting Works or SLW
Logo styles of interest
Emblem Logo
Look and feel

```html
<!DOCTYPE html>
<html lang="en">
<head>
<meta charset="utf-8">
<title>Stoneridge Lifting Works – Business Card Back</title>
<link rel="stylesheet" href="https://fonts.googleapis.com/css2?family=Archivo:wght@800&family=Roboto+Condensed:wght@500;700&display=swap">
<style>
  :root {
    --royal-blue: #3d50fb;
    --site-red: #e00a0a;
    --site-red-text: #e3201d;
    --silver: #a8b2b2;
    --silver-text: #c9cfcf;
    --address-text: #b9bff6;
    --steel-dark: #1f2323;
    --steel-mid: #2c3131;
    --ink: #0b0c0c;
  }
  html, body {
    margin: 0;
    padding: 0;
    width: 1200px;
    height: 741px;
    overflow: hidden;
    background: var(--ink);
  }
  .card {
    position: relative;
    width: 1200px;
    height: 741px;
    overflow: hidden;
    background: var(--ink);
    font-family: "Roboto Condensed", "Arial Narrow", sans-serif;
  }
  .web-band {
    position: absolute;
    left: 0; top: 0;
    width: 1200px; height: 182px;
    background: var(--royal-blue);
  }
  .web-address {
    position: absolute;
    left: 75px; top: 92px;
    margin: 0;
    font-family: "Archivo", "Arial Black", sans-serif;
    font-weight: 800;
    font-size: 62px;
    letter-spacing: -0.5px;
    line-height: 1;
    color: var(--ink);
  }
  .divider-strip {
    position: absolute;
    left: 0; top: 182px;
    width: 1200px; height: 20px;
    background: var(--ink);
  }
  .steel-frame-photo {
    position: absolute;
    left: 0; top: 202px;
    width: 1178px; height: 532px;
    background:
      radial-gradient(ellipse at 70% 30%, var(--steel-mid) 0%, var(--steel-dark) 55%, #151818 100%);
  }
  .contact-row {
    position: absolute;
    left: 0;
    height: 50px;
    display: flex;
    align-items: center;
    font-weight: 700;
    font-size: 30px;
    white-space: nowrap;
  }
  .contact-label {
    box-sizing: border-box;
    height: 50px;
    display: flex;
    align-items: center;
    padding-left: 75px;
    color: var(--ink);
  }
  .contact-detail {
    padding-left: 12px;
    font-weight: 500;
  }
  .site-contact { top: 265px; }
  .site-contact .contact-label { width: 289px; background: var(--site-red); }
  .site-contact .contact-detail { color: var(--site-red-text); }
  .office-contact { top: 349px; }
  .office-contact .contact-label { width: 289px; background: var(--silver); }
  .office-contact .contact-detail { color: var(--silver-text); }
  .hire-address { top: 577px; }
  .hire-address .contact-label { width: 570px; background: var(--royal-blue); }
  .hire-address .contact-detail { color: var(--address-text); padding-left: 22px; }
</style>
</head>
<body>
  <main class="card">
    <div class="steel-frame-photo" role="img" aria-label="Dark photograph of a structural steel frame with criss-crossing beams"></div>
    <header class="web-band">
      <h1 class="web-address">www.slwlifting.com</h1>
    </header>
    <div class="divider-strip"></div>

    <div class="contact-row site-contact">
      <span class="contact-label">Site Contact:</span>
      <span class="contact-detail">Danny Pruett - 0491 637 205 - dan@slwlifting.com</span>
    </div>

    <div class="contact-row office-contact">
      <span class="contact-label">Office Contact:</span>
      <span class="contact-detail">Leoni Marsh - 0437 918 542 - leoni@slwlifting.com</span>
    </div>

    <div class="contact-row hire-address">
      <span class="contact-label">Equipment &amp; Crane Hire Address:</span>
      <span class="contact-detail">27 Carvell Street, Mondarra Q 4612</span>
    </div>
  </main>
</body>
</html>
```